Ladies in Trade Global

We will be building the site using Dot Net Nuke content management system so design needs to be DNN compatible including fonts used.
Client has a site already www.ladiesintradeglobal.example
The overall look and feel desired by the client is for a professional yet social website. The website is to reflect the networking and professional training aspect of the clients business.
Pink and purple would be the dominant colours best used with white to maintain the clean professional feel.
Client likes www.galsofcommerce.example as an example
Images to use should be anything networking and awards type, I have attached their logo.
Homepage Layout
- Banner across the top with logo top left
- Horizontal navigation bar
- Newsletter sign up in the banner area
- Join facebook/twitter
- A large area for rotating images
- A side panel for upcoming events/training
- Room to put sponsors logo’s across bottom of page.
Content page Layout
- Will not need the large area for rotating images
- Join Facebook/Twitter
- Room for content
- Side Panel to out in newsletter signup and upcoming events
Sitemap
o Home
o About Us
o History
o Events
? -International Women’s Day
? - Guidance Medal
? - Skills and Careers Fair
? - Rosy Day
? - Networking Gallery
o Membership
? - Why Join?
? - Membership Form
o Training
? - Computer Training
? - Function Planning Academy
? - KQR Junior Scheme
o Latest News
? - Media Articles
? - Current Newsletter
? - Links
o Blog
o Contact Us
Hi everyone
Thanks you so much for submitting designs, I will be presenting them to my client on Monday so will let you know feedback after that.
Cheers
Tamsin
Hi designers
We gave the designs to our client before xmas but due to xmas/new year break they haven't responded as yet. We get back on 10th January so we sould have a respose from them by then.
Thanks for your patience.
Cheers
Tamsin
Hi everyone
Thanks for your patience we have had some major flooding in SE QLD so has closed a lot of businesses down until yesterday, we are hoping to meet with our client this week to select a design.
Cheers
Tamsin
Hi everyone
I appreciate your patience with this project.....I am still waiting on my client to make a decision on design am hoping it will be next week so I can close this project.
Cheers
Tamsin
Hi everyone
I've finally heard back from the client who have now been caught in Cyclone Omba.....but they have told me they will be selecting a design next Tuesday so I will let you know outcome asap.
Apologies for the delay with this project.
Thanks
Tamsin

```html
<!DOCTYPE html>
<html lang="en">
<head>
<meta charset="utf-8">
<title>Ladies in Trade Global</title>
<link href="https://fonts.googleapis.com/css2?family=Cinzel:wght@700&family=PT+Sans:wght@400;700&family=PT+Sans+Narrow:wght@400;700&display=swap" rel="stylesheet">
<style>
:root{
  --page:#ffffff;
  --magenta:#a3176e;
  --magenta-dark:#6b0a44;
  --magenta-deep:#8a0f5c;
  --pink:#e26aaa;
  --pink-soft:#f3bcd9;
  --pink-pale:#fbe3f0;
  --plum-text:#7a0f52;
  --white:#ffffff;
  --panel:rgba(255,255,255,.93);
}
*{margin:0;padding:0;box-sizing:border-box}
html,body{width:1200px;height:900px;overflow:hidden;background:var(--page)}
body{position:relative;font-family:"PT Sans Narrow",Arial,sans-serif}
.site{position:absolute;left:147px;top:4px;width:900px;height:896px;overflow:hidden;
  background:linear-gradient(180deg,#c94b92 0px,#b02a7c 240px,#9b1a6b 420px,#7e0d55 600px,#650843 720px,#b3347e 780px,#d964a6 896px)}
.site>*{position:absolute}
.banner{left:0;top:0;width:900px;height:226px}
.photo{left:460px;top:0;width:300px;height:224px;
  background:radial-gradient(ellipse at 55% 45%,#f0c7a8 0%,#e7b08d 25%,#c98b6b 45%,rgba(230,160,200,0) 75%)}
.auth{top:0;height:27px;width:73px;border-radius:0 0 12px 12px;
  background:linear-gradient(180deg,#d2509a,#a3176e);color:var(--white);
  font-family:"Cinzel",serif;font-size:13px;font-weight:700;text-align:center;line-height:28px;
  box-shadow:0 2px 3px rgba(90,0,50,.35)}
.auth.signup{left:343px}
.auth.login{left:424px;width:67px}
.brand{left:144px;top:22px;width:160px;text-align:center}
.brand-mark{position:absolute;left:8px;top:-12px;width:140px;height:140px;border-radius:50%;
  background:radial-gradient(circle,rgba(255,255,255,.65),rgba(240,190,220,.45))}
.brand-name{position:relative;font-family:"Cinzel",serif;font-weight:700;color:var(--magenta);
  font-size:26px;line-height:25px;letter-spacing:-.5px}
.welcome{left:190px;top:156px;font-family:"Cinzel",serif;font-weight:700;color:var(--magenta);font-size:18px;line-height:25px}
.welcome span{display:block;padding-left:62px}
.nav{left:144px;top:227px;height:60px;display:flex;list-style:none;border-left:1px solid rgba(255,255,255,.35)}
.nav li{position:relative;height:60px;border-right:1px solid rgba(255,255,255,.35);
  color:var(--white);font-family:"PT Sans",Arial,sans-serif;font-weight:700;font-size:10px;letter-spacing:-.4px;
  text-align:center;line-height:88px;text-transform:uppercase;
  background:linear-gradient(180deg,rgba(255,255,255,.08),rgba(255,255,255,0))}
.nav li.active{background:linear-gradient(180deg,#8d0a5d,#b8267d 90%,rgba(200,80,150,.4))}
.nav li.open{background:linear-gradient(180deg,#d68bbb,#c4649f)}
.submenu{left:338px;top:281px;width:112px;background:rgba(246,205,228,.95);list-style:none;padding:3px 0}
.submenu li{font-family:"PT Sans",Arial,sans-serif;font-weight:700;font-size:6px;color:var(--magenta);
  text-transform:uppercase;padding:0 5px;line-height:14.6px;letter-spacing:-.2px}
.content{left:140px;top:297px;width:418px;height:446px;background:rgba(255,255,255,.22)}
.content h1{height:23px;background:var(--white);color:var(--magenta);font-family:"PT Sans",Arial,sans-serif;
  font-weight:700;font-size:17px;letter-spacing:-1px;padding-left:13px;line-height:24px}
.copy{padding:4px 9px 0 9px;color:var(--white);font-family:"PT Sans",Arial,sans-serif;font-size:7.4px;line-height:10.4px;letter-spacing:-.15px}
.copy p{margin-bottom:10.4px}
.copy h2{font-size:7.4px;font-weight:700;color:#2b0018;text-transform:uppercase}
.pill{height:22px;border-radius:11px;background:linear-gradient(180deg,#f4a9d0,#de65a6);
  color:var(--white);font-family:"PT Sans",Arial,sans-serif;font-weight:700;font-size:14px;letter-spacing:-1px;
  text-align:center;line-height:22px;box-shadow:0 2px 3px rgba(90,0,50,.35)}
.box{background:var(--panel);border-radius:0 0 10px 10px}
.events-title{left:567px;top:305px;width:194px}
.events{left:580px;top:327px;width:167px;height:136px;padding:6px 6px 0 7px}
.event{display:flex;font-family:"PT Sans",Arial,sans-serif;font-size:6.5px;line-height:9.6px;letter-spacing:-.3px;margin-bottom:10px}
.event dt{width:55px;color:var(--magenta);font-weight:700}
.event dd{width:100px;color:#7a4b66}
.find-title{left:567px;top:472px;width:194px}
.find{left:580px;top:494px;width:167px;height:51px}
.join{position:absolute;left:12px;top:8px;font-family:"PT Sans",Arial,sans-serif;font-weight:700;color:var(--magenta);
  font-size:17px;line-height:16px;letter-spacing:-1px}
.social{position:absolute;top:10px;width:32px;height:32px;border-radius:5px;background:linear-gradient(180deg,#e98ac0,#b8267d)}
.social.one{left:81px}.social.two{left:121px}
.curve{left:0;top:600px;width:900px;height:200px}
.sponsors-title{left:221px;top:780px;width:425px}
.sponsors{left:233px;top:801px;width:402px;height:49px;background:var(--white);border-radius:0 0 12px 12px}
.sponsor{position:absolute;top:6px;height:36px}
.sponsor.one{left:50px;width:120px;background:#2b2b2b;height:26px;top:10px;border-radius:2px}
.sponsor.two{left:184px;width:70px;background:#c9a24d;border-radius:50%;width:36px;left:200px}
.sponsor.three{left:275px;width:64px;background:#f4e8ee;border:1px solid #e2c9d6}
.footer{left:0;top:864px;width:900px;text-align:center;color:var(--white);font-family:"PT Sans",Arial,sans-serif;
  font-weight:700;font-size:7px;letter-spacing:-.3px;line-height:10px;text-transform:uppercase}
</style>
</head>
<body>
<div class="site">
  <svg class="banner" viewBox="0 0 900 226" aria-hidden="true">
    <defs>
      <linearGradient id="sky" x1="0" y1="0" x2="0" y2="1">
        <stop offset="0" stop-color="#fbe6f1"/><stop offset="1" stop-color="#f7d3e6"/>
      </linearGradient>
      <linearGradient id="swoosh" x1="0" y1="0" x2="1" y2="0">
        <stop offset="0" stop-color="#d4589b"/><stop offset=".5" stop-color="#f4bcdb"/><stop offset="1" stop-color="#e07ab4"/>
      </linearGradient>
    </defs>
    <rect width="900" height="226" fill="url(#sky)"/>
    <path d="M0 40 C160 150 420 150 900 30 L900 0 L0 0Z" fill="#fdf1f7"/>
    <path d="M0 70 C200 160 500 130 900 60 L900 90 C500 160 250 190 0 120Z" fill="url(#swoosh)" opacity=".75"/>
    <path d="M0 120 C200 190 500 170 900 110 L900 226 L0 226Z" fill="#ec9cc7"/>
    <path d="M0 150 C260 215 560 200 900 140 L900 226 L0 226Z" fill="#f7d6e8"/>
    <path d="M560 0 C700 60 820 40 900 0Z" fill="#e27ab3" opacity=".6"/>
  </svg>
  <div class="photo" role="img" aria-label="Photo of two smiling businesswomen, one on a phone"></div>
  <a class="auth signup">Sign Up</a>
  <a class="auth login">Login</a>
  <div class="brand">
    <span class="brand-mark"></span>
    <div class="brand-name">Ladies in Trade Global</div>
  </div>
  <div class="welcome">Welcome to Ladies<span>in Trade Global</span></div>

  <svg class="curve" viewBox="0 0 900 200" aria-hidden="true">
    <path d="M0 110 C250 170 650 170 900 110 L900 200 L0 200Z" fill="#c74590"/>
    <path d="M0 140 C250 190 650 190 900 140 L900 200 L0 200Z" fill="#e07ab4"/>
  </svg>

  <ul class="nav">
    <li style="width:61px">Home</li>
    <li class="active" style="width:67px">About Us</li>
    <li style="width:65px">History</li>
    <li class="open" style="width:61px">Events</li>
    <li style="width:77px">Membership</li>
    <li style="width:67px">Training</li>
    <li style="width:81px">Latest News</li>
    <li style="width:56px">Blog</li>
    <li style="width:81px">Contact Us</li>
  </ul>

  <section class="content">
    <h1>WHAT WE DO</h1>
    <div class="copy">
      <p>Ladies in Trade Global is a membership organisation offering networking, training and employment opportunities to women and the community.</p>
      <h2>Networking</h2>
      <p>Our networking division is supported by individual and corporate memberships and sponsorships.</p>
      <p>In recent years, we have established solid partnerships with such organisations as Bellmoor Wellness Retreat, Harwick University, Sandport Council, Sandport Tourism Corporation and Lilypad Institute.</p>
      <p>With their assistance, we have been able to host such innovative events as the Annual Sandport International Women's Day Festival, women's employment and training expos and our annual Guidance Medal program.</p>
      <p>Ladies in Trade Global is also well-supported by individual memberships. Our members consist of thousands of women who value the business – and company – of other women.</p>
      <p>Our functions – breakfasts, luncheons, dinners – are exciting get-togethers that begin with networking opportunities that quickly turn to friendships.</p>
      <p>The Ladies in Trade Global philosophy of inclusion, and our commitment to the meaningful participation of women in the workforce, has united the aims of our supporters with the commercial heart of the nation's businesses.</p>
      <p>Join us – and you too will make a difference for other women!</p>
      <h2>Training</h2>
      <p>Ladies in Trade's training division – Training Academy for Women, is based on what we call 'the three Cs' – computers, confidence and career advice.</p>
      <p>Our research has shown that these are the most probable reasons for women's unemployment or under-employment.</p>
      <p>In fact, our most recent study found that the greatest barrier to re-entering the workforce for 77 per cent of Queensland women was computer illiteracy.</p>
      <p>Consequently, Ladies in Trade holds ongoing computer training courses for everyone from absolute beginners to those who want to update existing skills.</p>
      <p>We also harness the energies of our event, to assist us with hosting such events as our International Women's Day Festival, our Ladies in Trade Skills and Careers Fair and our annual Ladies in Trade Guidance Medal.</p>
    </div>
  </section>

  <ul class="submenu">
    <li>International Women's Day</li>
    <li>Guidance Medal</li>
    <li>Skills and Careers Fair</li>
    <li>Rosy Day</li>
    <li>Networking Gallery</li>
  </ul>

  <div class="pill events-title">UPCOMING EVENT</div>
  <dl class="box events">
    <div class="event"><dt>September</dt><dd>Nominations open for the 2011 International Women's Day Leadership and Youth Guidance Medal</dd></div>
    <div class="event"><dt>Oktober</dt><dd>Pink Breakfast with Ladies in Travel Inc</dd></div>
    <div class="event"><dt>December</dt><dd>Palazzo Verano – Ladies in Trade Xmas Party</dd></div>
    <div class="event"><dt>March</dt><dd>IWD Festival – 7th to 12th March</dd></div>
  </dl>

  <div class="pill find-title">FIND US!</div>
  <div class="box find">
    <div class="join">JOIN US<br>NOW!!</div>
    <span class="social one" role="img" aria-label="Social network link"></span>
    <span class="social two" role="img" aria-label="Social network link"></span>
  </div>

  <div class="pill sponsors-title">OUR SPONSORS</div>
  <div class="sponsors">
    <span class="sponsor one" role="img" aria-label="Sponsor badge"></span>
    <span class="sponsor two" role="img" aria-label="Sponsor badge"></span>
    <span class="sponsor three" role="img" aria-label="Sponsor badge"></span>
  </div>

  <div class="footer">Privacy | Terms and Conditions | Sitemap | Contact Us | Advertise<br>Copyright – Ladies in Trade Global 2010</div>
</div>
</body>
</html>
```